postcard for Real Estate Agent that sells homes for less than any other agents

My company sells houses for a fraction of what others charge. I have most of the verbiage but I am open to ideas.
Our post card will be 6.25 x 9
We need an image that goes with our words and draws people to take a look
We are playful at the same time very serious about the money we will save our clients. In the past our message has been received as too good to be true. Our old message was "save $6000* when you list with us" We think the "*" was causing people to think their was a catch. Other agents will tell people that we will not do what they will do and that is why they must charge more. We are a full service agency and we will generally do everything that other agents will do and in many cases we will do more than other agents. We are changing this industry and need our message to get to every person that is thinking of selling their home

Target Market(s)

People who want to list their home for sale

Industry/Entity Type

Real Estate Agent

Requirements
Must have
• Image that makes people read the message

```html
<!DOCTYPE html>
<html lang="en">
<head>
<meta charset="utf-8">
<title>Hearthline Listing Postcard</title>
<link rel="stylesheet" href="https://fonts.googleapis.com/css2?family=Oswald:wght@500;600&family=Arimo:wght@400;700&family=Lato:ital,wght@0,400;0,700;1,700&display=swap">
<style>
  :root{
    --navy:#1c4583;
    --blue:#2563b8;
    --blue-light:#3a7fd4;
    --green:#6cc72f;
    --green-dark:#4ea61c;
    --ink:#2a2a2a;
    --white:#ffffff;
    --page:#e9ecef;
    --rule:#bcbcbc;
  }
  *{box-sizing:border-box;margin:0;padding:0}
  html,body{width:902px;height:1200px;overflow:hidden;background:var(--page)}
  body{position:relative;font-family:"Lato",sans-serif;color:var(--ink)}

  .card{position:absolute;left:40px;width:822px;height:560px;background:var(--white);box-shadow:0 2px 8px rgba(0,0,0,.18);overflow:hidden}
  .card--front{top:30px}
  .card--back{top:620px}

  /* FRONT */
  .offer-panel{position:absolute;left:0;top:0;width:265px;height:460px;
    background:linear-gradient(180deg,var(--blue-light) 0%,var(--blue) 30%,var(--navy) 100%);
    clip-path:polygon(0 0,100% 0,100% 100%,0 93%);z-index:2}
  .offer-save{position:absolute;top:30px;width:100%;text-align:center;font-family:"Oswald",sans-serif;font-weight:600;font-size:52px;color:var(--white);line-height:1}
  .offer-amount{position:absolute;top:92px;width:100%;text-align:center;font-family:"Oswald",sans-serif;font-weight:600;font-size:86px;line-height:1;color:var(--green);letter-spacing:-1px}
  .offer-amount .dollar{color:var(--white)}
  .offer-rule{position:absolute;top:205px;left:24px;right:24px;height:1px;background:rgba(255,255,255,.7)}
  .offer-line{position:absolute;top:216px;width:100%;text-align:center;font-family:"Arimo",sans-serif;font-size:33px;line-height:42px;color:var(--white)}
  .crazy-ribbon{position:absolute;left:0;top:308px;width:283px;height:90px;z-index:3;
    background:linear-gradient(180deg,#8ad84a,var(--green-dark));text-align:center;font-family:"Arimo",sans-serif;padding-top:5px}
  .crazy-ribbon .lead{font-size:24px;color:var(--white);line-height:28px}
  .crazy-ribbon .shout{font-size:24px;color:#1d1d1d;line-height:28px}
  .crazy-ribbon .small{font-size:12.5px;font-weight:700;color:#1d1d1d;line-height:18px}

  .hero-photo{position:absolute;left:250px;top:0;right:0;height:500px;
    background:linear-gradient(160deg,#dfe7ee 0%,#b7c6d2 45%,#7f9a7d 100%)}
  .hero-swoosh{position:absolute;left:250px;top:380px;width:572px;height:130px;z-index:1}

  .brand{position:absolute;display:flex;align-items:center;gap:8px;font-family:"Lato",sans-serif;font-weight:700;color:var(--navy)}
  .brand .mark{width:18px;height:18px;background:var(--green)}
  .card--front .brand{left:26px;top:500px;font-size:24px}

  .contact-line{position:absolute;left:268px;top:520px;font-family:"Lato",sans-serif;font-size:17px;white-space:nowrap}
  .contact-line .cue{color:var(--green-dark);font-style:italic;font-weight:700}
  .contact-line .detail{color:var(--ink);font-weight:700}
  .contact-line .or{color:var(--navy);font-style:italic;font-weight:700;margin:0 20px}

  /* BACK */
  .mail-panel{position:absolute;left:0;top:0;width:385px;height:490px;border-right:6px solid var(--navy)}
  .home-photo{position:absolute;left:0;top:0;width:379px;height:190px;
    background:linear-gradient(180deg,#9fb4d6 0%,#c7c9d6 45%,#8c8a82 78%,#5b7a3e 100%)}
  .photo-rule{position:absolute;left:0;top:190px;width:379px;height:3px;background:var(--green)}
  .ideas-title{position:absolute;left:20px;top:203px;font-family:"Arimo",sans-serif;font-weight:700;font-size:24px;color:#222}
  .ideas-sub{position:absolute;left:20px;top:234px;font-family:"Lato",sans-serif;font-style:italic;font-weight:700;font-size:18px;color:var(--green-dark)}
  .idea-list{position:absolute;list-style:none;font-family:"Lato",sans-serif;font-style:italic;font-weight:700;font-size:11px;color:#2b2b2b}
  .idea-list li{height:19px;padding-left:12px;position:relative}
  .idea-list li::before{content:"";position:absolute;left:0;top:3px;width:7px;height:7px;border-radius:50%;background:var(--green)}
  .card--back .brand{left:266px;top:360px;font-size:16px}
  .card--back .brand .mark{width:13px;height:13px}

  .mail-footer{position:absolute;left:0;top:403px;width:379px;height:87px;background:var(--navy)}
  .mail-footer .tagline{position:absolute;left:20px;top:11px;width:190px;font-style:italic;font-weight:700;font-size:12px;line-height:15px;color:var(--green)}
  .mail-footer .phone{position:absolute;left:24px;top:50px;display:flex;align-items:center;gap:14px;font-family:"Lato",sans-serif;font-size:18px;color:var(--white)}
  .mail-footer .follow{position:absolute;left:272px;top:22px;font-size:15px;color:var(--white)}
  .mail-footer .social{position:absolute;left:282px;top:46px;display:flex;gap:12px}
  .mail-footer .social span{width:26px;height:26px;border-radius:50%;background:var(--white)}

  .stamp-box{position:absolute;left:614px;top:48px;width:120px;height:135px;border:1px solid var(--rule)}
  .address-line{position:absolute;left:431px;width:303px;height:1px;background:var(--rule)}
</style>
</head>
<body>

<section class="card card--front">
  <div class="hero-photo" role="img" aria-label="Smiling couple holding fans of cash in front of a light grey two-storey house"></div>
  <svg class="hero-swoosh" viewBox="0 0 572 130" preserveAspectRatio="none" aria-hidden="true">
    <path d="M0 70 C180 130 380 120 572 30 L572 130 L0 130 Z" fill="#6cc72f"/>
    <path d="M0 84 C190 140 390 132 572 50 L572 130 L0 130 Z" fill="#ffffff"/>
  </svg>

  <div class="offer-panel">
    <div class="offer-save">SAVE</div>
    <div class="offer-amount"><span class="dollar">$</span>6000</div>
    <div class="offer-rule"></div>
    <div class="offer-line">When you<br>list with us</div>
  </div>
  <div class="crazy-ribbon">
    <div class="lead">You’d have to be</div>
    <div class="shout">Bat $#@T CRAZY</div>
    <div class="small">To give an agent $6000.00</div>
  </div>

  <div class="brand"><span class="mark"></span>Hearthline</div>

  <p class="contact-line">
    <span class="cue">Call Dan or Mark at</span> <span class="detail">555-014-2290</span>
    <span class="or">Or</span>
    <span class="cue">Visit</span>&nbsp;&nbsp;<span class="detail">www.Hearthline.com</span>
  </p>
</section>

<section class="card card--back">
  <div class="mail-panel">
    <div class="home-photo" role="img" aria-label="Large suburban family home with lit windows and double garage at dusk"></div>
    <div class="photo-rule"></div>
    <h2 class="ideas-title">To put a sign in your yard</h2>
    <p class="ideas-sub">Look at what you can do with $6000.00</p>

    <ul class="idea-list" style="left:22px;top:270px">
      <li>Give it to your Kids</li><li>Build a fence</li><li>Build a deck</li>
    </ul>
    <ul class="idea-list" style="left:146px;top:270px">
      <li>Landscape</li><li>Take a Vacation</li><li>Buy new clothes</li>
    </ul>
    <ul class="idea-list" style="left:267px;top:270px">
      <li>Landscape</li><li>Take a Vacation</li><li>Buy new clothes</li>
    </ul>
    <ul class="idea-list" style="left:22px;top:338px">
      <li>Pay off your car</li><li>Pay off student loan</li>
    </ul>
    <ul class="idea-list" style="left:146px;top:338px">
      <li>Buy New Carpet</li><li>Upgrade Appliance</li>
    </ul>

    <div class="brand"><span class="mark"></span>Hearthline</div>

    <div class="mail-footer">
      <p class="tagline">Full Service Agency at a Fraction of the Cost</p>
      <p class="phone">
        <svg width="22" height="22" viewBox="0 0 24 24" aria-hidden="true"><path d="M6.6 10.8a15 15 0 0 0 6.6 6.6l2.2-2.2a1 1 0 0 1 1-.25 11.4 11.4 0 0 0 3.6.57 1 1 0 0 1 1 1V20a1 1 0 0 1-1 1A17 17 0 0 1 3 4a1 1 0 0 1 1-1h3.5a1 1 0 0 1 1 1c0 1.25.2 2.45.57 3.57a1 1 0 0 1-.25 1z" fill="#fff"/></svg>
        555-014-2290
      </p>
      <p class="follow">Follow Us on</p>
      <div class="social"><span></span><span></span></div>
    </div>
  </div>

  <div class="stamp-box"></div>
  <div class="address-line" style="top:254px"></div>
  <div class="address-line" style="top:319px"></div>
  <div class="address-line" style="top:378px"></div>
</section>

</body>
</html>
```